Book Cover Contest: "Rivers Toward a Calm Dawn"

The KT Verlag Islamic Library invites designers and artists to design a cover for the upcoming book “Rivers Toward a Calm Dawn”.

This inspiring work is by Shaikh Umar al-Fadil ibn Yusuf ibn Hamzah al-Qurtubi (d. 1376 AH/1957 CE), a renowned Islamic scholar. In his writing, he imparts timeless principles for inner peace and true happiness based on Islamic faith and spiritual knowledge.

Important details for the cover design:
The cover should reflect the theme of the book: paths to happiness, spiritual satisfaction, a fulfilled life.
It may contain both modern and traditional elements, but should be clear, appealing and reader-friendly.
The title “Rivers toward a calm dawn” should be clearly visible.
Author: Šaiḫ ʿUmar al-Fāḍil ibn Yūsuf ibn Ḥamzah al-Qurṭubī
Translation: Marita Lohse

KT Verlag Islamic Library

Do you have a creative idea for the cover? Then join in and design the face of this inspiring work!

Target Market(s)

Islamic

Font styles to use
Decorative
Script

Requirements
Should not have
• No mosque silhouette, no hanging lamp,

```html
<!DOCTYPE html>
<html lang="en">
<head>
<meta charset="utf-8">
<title>Rivers Toward a Calm Dawn — Book Cover</title>
<link rel="stylesheet" href="https://fonts.googleapis.com/css2?family=Cinzel:wght@400;600;700&display=swap">
<style>
  :root {
    --stage: #000000;
    --paper: #e6e7e8;
    --emerald: #00614f;
    --gold: #d4af61;
    --white: #ffffff;
    --ink-green: #00614f;
  }
  * { margin: 0; padding: 0; box-sizing: border-box; }
  html, body {
    width: 1137px;
    height: 1200px;
    overflow: hidden;
    background: var(--stage);
  }
  .cover {
    position: absolute;
    left: 190px;
    top: 32px;
    width: 758px;
    height: 1137px;
    background: var(--paper);
    overflow: hidden;
    font-family: "Cinzel", serif;
  }
  .gold-rule {
    position: absolute;
    background: var(--gold);
  }
  .gold-rule--top { left: 159px; top: 115px; width: 436px; height: 28px; }
  .gold-rule--mid { left: 44px; top: 613px; width: 665px; height: 27px; }
  .title-band {
    position: absolute;
    left: 0;
    top: 148px;
    width: 100%;
    height: 386px;
    background: var(--emerald);
  }
  .title {
    position: absolute;
    left: 0;
    top: 188px;
    width: 100%;
    text-align: center;
    white-space: nowrap;
  }
  .title__lead {
    display: block;
    color: var(--white);
    font-weight: 400;
    font-size: 56px;
    letter-spacing: 3px;
    line-height: 60px;
  }
  .title__main {
    display: block;
    margin-top: 10px;
    color: var(--gold);
    font-weight: 700;
    font-size: 92px;
    letter-spacing: 0;
    line-height: 120px;
  }
  .title__initial { font-size: 120px; }
  .emblem {
    position: absolute;
    left: 101px;
    top: 394px;
    width: 560px;
    height: 560px;
  }
  .emblem__frame { fill: var(--white); filter: drop-shadow(0 2px 6px rgba(0,0,0,0.25)); }
  .emblem__line { fill: none; stroke: var(--gold); stroke-width: 2; }
  .author {
    position: absolute;
    left: 0;
    top: 960px;
    width: 100%;
    text-align: center;
    color: var(--ink-green);
    font-weight: 600;
    font-size: 34px;
    line-height: 40px;
    letter-spacing: 0.5px;
    white-space: nowrap;
  }
  .translator {
    position: absolute;
    left: 0;
    top: 1066px;
    width: 100%;
    text-align: center;
    color: var(--ink-green);
    font-weight: 600;
    font-size: 19px;
    letter-spacing: 0.5px;
  }
</style>
</head>
<body>
  <main class="cover">
    <div class="gold-rule gold-rule--top"></div>
    <div class="title-band"></div>
    <h1 class="title">
      <span class="title__lead">RIVERS TOWARD A</span>
      <span class="title__main"><span class="title__initial">C</span>ALM <span class="title__initial">D</span>AWN</span>
    </h1>
    <div class="gold-rule gold-rule--mid"></div>

    <svg class="emblem" viewBox="-280 -280 560 560" xmlns="http://www.w3.org/2000/svg">
      <defs>
        <linearGradient id="scene-tones" x1="0" y1="0" x2="0" y2="1">
          <stop offset="0" stop-color="#2a1a24"/>
          <stop offset="0.35" stop-color="#5a2030"/>
          <stop offset="0.6" stop-color="#8fc8cf"/>
          <stop offset="1" stop-color="#3d4a55"/>
        </linearGradient>
      </defs>
      <polygon class="emblem__frame"
        points="270.1,0 191,79.1 191,191 79.1,191 0,270.1 -79.1,191 -191,191 -191,79.1 -270.1,0 -191,-79.1 -191,-191 -79.1,-191 0,-270.1 79.1,-191 191,-191 191,-79.1"/>
      <polygon class="emblem__line"
        points="248.9,0 176,72.9 176,176 72.9,176 0,248.9 -72.9,176 -176,176 -176,72.9 -248.9,0 -176,-72.9 -176,-176 -72.9,-176 0,-248.9 72.9,-176 176,-176 176,-72.9"/>
      <polygon role="img" aria-label="Photograph of whirling dervishes in white robes dancing under red light"
        fill="url(#scene-tones)"
        points="227.7,0 161,66.7 161,161 66.7,161 0,227.7 -66.7,161 -161,161 -161,66.7 -227.7,0 -161,-66.7 -161,-161 -66.7,-161 0,-227.7 66.7,-161 161,-161 161,-66.7"/>
    </svg>

    <p class="author">Šaiḫ ʿUmar al-Fāḍil<br>ibn Yūsuf ibn Ḥamzah al-Qurṭubī</p>
    <p class="translator">Translation: Marita Lohse</p>
  </main>
</body>
</html>
```